Contractor Business Card Design

Looking to have a card made that has a bold description of (KITCHENS, BASEMENTS, BATHROOMS)

Definition and layers a plus

Contact info is;

Mark T. Ellery
Larkdale, MN 55990
Cell: 612-555-0147
website: www.cobaltfinishworks.example
Email: cobaltfinishworksmn@mailbox.example

colors: red, black, gray, white

Contact Information for Business Card

Contact info is;

Mark T. Ellery
Larkdale, MN 55990
Cell: 612-555-0147

Colors
ec1f27

Requirements
Must have
• Looking for layers and definition
Nice to have
• Cards are planned to be printed on plastic cards

```html
<!DOCTYPE html>
<html lang="en">
<head>
<meta charset="utf-8">
<title>Cobalt Finish Works – Business Card</title>
<link href="https://fonts.googleapis.com/css2?family=Poppins:wght@400;500;600;700&display=swap" rel="stylesheet">
<style>
  :root {
    --stage: #141414;
    --card: #1b1b1b;
    --card-edge: #262626;
    --red: #ec1f27;
    --white: #f4f4f4;
    --gray: #8a8a8a;
    --faint: rgba(255,255,255,0.05);
  }
  * { margin: 0; padding: 0; box-sizing: border-box; }
  html, body {
    width: 1200px; height: 1200px; overflow: hidden;
    background: radial-gradient(circle at 50% 20%, #262626 0%, var(--stage) 70%);
    font-family: "Poppins", sans-serif;
    color: var(--white);
  }
  .card {
    position: absolute;
    left: 180px;
    width: 840px; height: 480px;
    background: var(--card);
    border: 1px solid var(--card-edge);
    border-radius: 22px;
    box-shadow: 0 24px 50px rgba(0,0,0,0.6);
    overflow: hidden;
  }
  .card--front { top: 80px; }
  .card--back { top: 640px; }

  /* brand block */
  .brand { display: flex; flex-direction: column; align-items: center; gap: 22px; }
  .brand__ring {
    width: 110px; height: 110px; border-radius: 50%;
    border: 5px solid var(--red);
  }
  .brand__name {
    font-weight: 700; font-size: 40px; letter-spacing: 2px;
    color: var(--white); text-transform: uppercase; line-height: 1;
    text-align: center; white-space: nowrap;
  }

  .card--front .brand { position: absolute; top: 90px; left: 0; right: 0; }
  .services {
    position: absolute; left: 0; right: 0; top: 370px;
    display: flex; justify-content: center; align-items: center; gap: 18px;
    font-weight: 700; font-size: 22px; letter-spacing: 1px;
  }
  .services__dot {
    width: 16px; height: 16px; border-radius: 50%;
    border: 2px solid var(--red);
  }

  /* back */
  .card--back .brand { position: absolute; left: 25px; top: 140px; width: 355px; }
  .card--back .brand__ring { width: 130px; height: 130px; }
  .card--back .brand__name { font-size: 24px; letter-spacing: 1.5px; }
  .divider {
    position: absolute; left: 400px; top: 100px;
    width: 1.5px; height: 280px;
    background: linear-gradient(var(--card), var(--gray) 50%, var(--card));
  }
  .watermark {
    position: absolute; right: -90px; top: 60px;
    width: 440px; height: 440px; border-radius: 50%;
    border: 12px solid var(--faint);
  }
  .contact { position: absolute; left: 430px; top: 150px; }
  .contact__name {
    font-weight: 700; font-size: 26px; letter-spacing: 1px;
    text-transform: uppercase; margin-bottom: 18px;
  }
  .contact__list { list-style: none; display: flex; flex-direction: column; gap: 12px; }
  .contact__item { display: flex; align-items: center; gap: 12px; font-size: 17px; white-space: nowrap; }
  .contact__icon { width: 20px; height: 20px; flex: none; }
</style>
</head>
<body>

<section class="card card--front">
  <div class="brand">
    <div class="brand__ring"></div>
    <div class="brand__name">Cobalt Finish Works</div>
  </div>
  <div class="services">
    <span>KITCHENS</span><span class="services__dot"></span>
    <span>BASEMENTS</span><span class="services__dot"></span>
    <span>BATHROOMS</span>
  </div>
</section>

<section class="card card--back">
  <div class="watermark"></div>
  <div class="brand">
    <div class="brand__ring"></div>
    <div class="brand__name">Cobalt Finish Works</div>
  </div>
  <div class="divider"></div>
  <div class="contact">
    <div class="contact__name">Mark T. Ellery</div>
    <ul class="contact__list">
      <li class="contact__item">
        <svg class="contact__icon" viewBox="0 0 20 20"><rect x="5" y="1.5" width="10" height="17" rx="2" fill="none" stroke="#ec1f27" stroke-width="2"/><line x1="8.5" y1="15" x2="11.5" y2="15" stroke="#ec1f27" stroke-width="1.5"/></svg>
        612 555 0147
      </li>
      <li class="contact__item">
        <svg class="contact__icon" viewBox="0 0 20 20"><rect x="1.5" y="4" width="17" height="12" rx="1" fill="#ec1f27"/><polyline points="2,5 10,11 18,5" fill="none" stroke="#1b1b1b" stroke-width="1.5"/></svg>
        cobaltfinishworksmn@mailbox.example
      </li>
      <li class="contact__item">
        <svg class="contact__icon" viewBox="0 0 20 20"><path d="M10 1a6.5 6.5 0 0 0-6.5 6.5C3.5 12.5 10 19 10 19s6.5-6.5 6.5-11.5A6.5 6.5 0 0 0 10 1z" fill="#ec1f27"/><circle cx="10" cy="7.5" r="2.3" fill="#1b1b1b"/></svg>
        Larkdale, MN 55990
      </li>
    </ul>
  </div>
</section>

</body>
</html>
```